BQN - New Homepage needed for an existing website

Lantern of Meridel Website
Need a new Homepage for an existing website with Action Items and Newer Pictures
This is the current Website
https://lanternofmeridel.example/

This new page will be changed on Jan 21st when Voting begins
1. Voting like a political campaign where we are trying to raise awareness for the issues we stand for and urge the people to go to a Polling /voting website and vote for us (Roster 27)
2. We have 6 basic themes as to what we stand for - there will be text to promote their importance of voting/call to action
3. There will be videos on the website and there will be a simulation of how the voting process works - will be added later

Use colors like the US Flag - Red, White and Blue. The other pages don't need to be changed - only the HomePage.

I only need the design, I will code the website. Thank you

Target Market(s)

Jewish People in the US

Industry/Entity Type

Religious

Number of Pages Required

1 page

Font styles to use
Serif
Sans Serif

Colors

Designer to choose colors to be used in the design.

Requirements
Must have
• Call to Action - Go out to Vote
• This is the current Website - https://lanternofmeridel.example/

```html
<!DOCTYPE html>
<html lang="en">
<head>
<meta charset="utf-8">
<title>Lantern of Meridel — Vote for Better Future</title>
<link href="https://fonts.googleapis.com/css2?family=Montserrat:wght@400;500;600;800;900&display=swap" rel="stylesheet">
<style>
  :root {
    --blue: #1c4a8a;
    --red: #b33425;
    --ink: #1d1d1f;
    --body: #2b2b2b;
    --white: #ffffff;
    --hero-gray: #8b8b8b;
    --hero-dark: #2e2e2e;
    --photo-light: #c9cbc9;
    --photo-dark: #2a2522;
  }
  * { margin: 0; padding: 0; box-sizing: border-box; }
  html, body {
    width: 1124px; height: 1200px; overflow: hidden;
    background: var(--white);
    font-family: "Montserrat", sans-serif;
    color: var(--body);
  }
  .site-header {
    height: 53px; display: flex; align-items: center;
    padding: 0 82px; justify-content: space-between;
    background: var(--white);
  }
  .brand { display: flex; align-items: center; gap: 7px; }
  .brand-mark { width: 16px; height: 16px; background: var(--blue); }
  .brand-name { font-weight: 600; font-size: 11px; color: var(--ink); }
  .main-nav { display: flex; gap: 22px; }
  .main-nav a {
    font-size: 7.6px; font-weight: 500; color: var(--ink); text-decoration: none;
  }
  .hero {
    position: relative; height: 375px;
    background: linear-gradient(100deg, var(--hero-gray) 0%, var(--hero-gray) 55%, #7a7a7a 75%, var(--hero-dark) 100%);
    box-shadow: 0 6px 12px rgba(0,0,0,.12);
  }
  .hero-photo { position: absolute; inset: 0; }
  .hero-band {
    position: absolute; left: 0; top: 60px; width: 585px; height: 64px;
    background: var(--blue); display: flex; align-items: center; padding-left: 82px;
  }
  .hero-band h1 {
    color: var(--white); font-weight: 900; font-size: 32.5px; letter-spacing: .6px;
  }
  .hero-lead {
    position: absolute; left: 82px; top: 152px; width: 460px;
    color: var(--white); font-size: 14.4px; line-height: 21px;
  }
  .btn-primary {
    position: absolute; left: 82px; top: 297px; width: 140px; height: 35px;
    background: var(--red); color: var(--white); border-radius: 2px;
    display: flex; align-items: center; justify-content: center;
    font-weight: 800; font-size: 11.5px; letter-spacing: .3px; text-decoration: none;
  }
  .slogan {
    height: 205px; display: flex; flex-direction: column; align-items: center; justify-content: center;
    font-weight: 900; font-size: 32.5px; line-height: 39px; letter-spacing: .8px;
    box-shadow: 0 6px 10px rgba(0,0,0,.06); position: relative;
  }
  .slogan .blue { color: var(--blue); }
  .slogan .red { color: var(--red); }
  .slogan .dark { color: var(--ink); }
  .mission {
    position: relative; height: 562px;
    box-shadow: 0 6px 10px rgba(0,0,0,.08);
  }
  .mission h2 {
    position: absolute; left: 82px; top: 70px;
    color: var(--blue); font-weight: 900; font-size: 32.5px; letter-spacing: .6px;
  }
  .mission-copy {
    position: absolute; left: 82px; top: 140px; width: 440px;
    font-size: 14.4px; line-height: 21px; color: var(--body);
  }
  .mission-copy p { margin-bottom: 21px; }
  .mission-photo {
    position: absolute; left: 562px; top: 75px; width: 480px; height: 384px;
    background: linear-gradient(160deg, var(--photo-light) 0%, #8e8c88 35%, var(--photo-dark) 70%, #3a3431 100%);
  }
</style>
</head>
<body>
  <header class="site-header">
    <div class="brand">
      <span class="brand-mark"></span>
      <span class="brand-name">Lantern of Meridel</span>
    </div>
    <nav class="main-nav">
      <a href="#">Confront Anti-Semitism</a>
      <a href="#">Expose BDS</a>
      <a href="#">Instill Jewish Pride</a>
      <a href="#">Israel: The Eternal Jewish Homeland</a>
      <a href="#">Maintain Israel's Jewish Identity</a>
      <a href="#">Resist Assimilation</a>
      <a href="#">New Law Increases Hate Crimes</a>
    </nav>
  </header>

  <section class="hero">
    <div class="hero-photo" role="img" aria-label="Hand dropping a ballot envelope into a voting box, in grey tones"></div>
    <div class="hero-band"><h1>VOTE FOR BETTER FUTURE</h1></div>
    <p class="hero-lead">Lantern of Meridel is committed to respecting our Jewish past and shared heritage and embracing its future.<br>Vote for us is vote for better future of Jewish People in the US!</p>
    <a class="btn-primary" href="#">LEARN MORE</a>
  </section>

  <section class="slogan">
    <span class="blue">SIX POINTS</span>
    <span class="red">FIVE MINUTES</span>
    <span class="dark">ONE BOLD NEW MOVEMENT</span>
  </section>

  <section class="mission">
    <h2>MISSION STATEMENT</h2>
    <div class="mission-copy">
      <p>Lantern of Meridel is a grassroots movement that was established to promote Jewish Continuity, recognizing that in the United States, Judaism and its continuity are under attack for a host of reasons, all of which Lantern of Meridel believes must be identified, understood, and addressed in the appropriate manner.</p>
      <p>Lantern of Meridel is non-political. We believe that all American Jews, regardless of ideological belief, can embrace the concept that in order to ensure the survival of the Jewish people there must be Jewish people.</p>
      <p>At the annual Passover Seder we say that “in every generation they stand ready to annihilate us ” - this is both historically accurate and currently relevant.</p>
    </div>
    <div class="mission-photo" role="img" aria-label="Group of young men in black hats and suits walking down a stone street with a boy in front"></div>
  </section>
</body>
</html>
```